Velnadex a Canadian Brand

I'm looking for a new name card design together with our new brand "Velnadex"! FYI, Velnadex is a new developed compounds for raw plastic material in order to improve the Physical properties。

Target Market(s)

Worldwide

Industry/Entity Type

Plastic

```html
<!DOCTYPE html>
<html lang="en">
<head>
<meta charset="utf-8">
<title>Velnadex Business Card</title>
<link rel="stylesheet" href="https://fonts.googleapis.com/css2?family=Exo+2:wght@400;500&family=Open+Sans:wght@400&display=swap">
<style>
  :root {
    --backdrop: #97989c;
    --card: #f2f2f4;
    --brand-blue: #1176bd;
    --deep-blue: #1e5f96;
    --swoosh-grey: #5a5a5c;
    --text-grey: #555558;
    --white: #ffffff;
  }
  html, body {
    margin: 0;
    padding: 0;
    width: 1200px;
    height: 1000px;
    overflow: hidden;
    background: var(--backdrop);
  }
  .canvas {
    position: relative;
    width: 1200px;
    height: 1000px;
  }
  .card {
    position: absolute;
    left: 322px;
    width: 556px;
    height: 325px;
    background: var(--card);
    box-shadow: 4px 5px 6px rgba(0,0,0,0.35);
    overflow: hidden;
  }
  .card--front { top: 139px; }
  .card--back { top: 514px; }
  .card svg.shapes {
    position: absolute;
    inset: 0;
    width: 556px;
    height: 325px;
  }
  .brand-name {
    position: absolute;
    font-family: "Exo 2", sans-serif;
    font-weight: 400;
    font-size: 31px;
    letter-spacing: 1px;
    color: var(--brand-blue);
    line-height: 1;
    margin: 0;
  }
  .card--front .brand-name { left: 45px; top: 50px; }
  .card--back .brand-name { left: 0; right: 0; top: 145px; text-align: center; }
  .person-name {
    position: absolute;
    left: 45px;
    top: 150px;
    margin: 0;
    font-family: "Exo 2", sans-serif;
    font-weight: 400;
    font-size: 22px;
    letter-spacing: 1.5px;
    color: var(--white);
    line-height: 1;
  }
  .person-title {
    position: absolute;
    left: 52px;
    top: 182px;
    margin: 0;
    font-family: "Open Sans", sans-serif;
    font-size: 14px;
    color: var(--white);
    line-height: 1;
  }
  .contact-list {
    position: absolute;
    top: 244px;
    margin: 0;
    padding: 0;
    list-style: none;
    font-family: "Open Sans", sans-serif;
    font-size: 15px;
    color: var(--text-grey);
  }
  .contact-list--phones { left: 51px; }
  .contact-list--web { left: 315px; }
  .contact-list li {
    display: flex;
    align-items: center;
    height: 21px;
  }
  .contact-list svg {
    width: 18px;
    height: 18px;
    margin-right: 10px;
    flex: none;
  }
</style>
</head>
<body>
<div class="canvas">

  <section class="card card--front">
    <svg class="shapes" viewBox="0 0 556 325" aria-hidden="true">
      <path d="M0,137 C250,134 400,114 485,0 L556,0 L556,217 L0,217 Z" fill="var(--brand-blue)"/>
      <rect x="0" y="205" width="556" height="12" fill="var(--deep-blue)"/>
      <path d="M0,137 C250,134 400,114 485,0" fill="none" stroke="var(--white)" stroke-width="6"/>
      <path d="M0,132 C248,129 394,109 478,0" fill="none" stroke="var(--swoosh-grey)" stroke-width="5"/>
    </svg>
    <p class="brand-name">Velnadex</p>
    <h1 class="person-name">YOUR NAME</h1>
    <p class="person-title">TITLE</p>
    <ul class="contact-list contact-list--phones">
      <li>
        <svg viewBox="0 0 18 18" aria-hidden="true"><circle cx="9" cy="9" r="9" fill="var(--brand-blue)"/><path d="M5.5,5 l2,0 l0.8,2.2 l-1.2,1 q1,2 3,3 l1,-1.2 l2.2,0.8 l0,2 q-6,0.5 -7.8,-7.8z" fill="var(--white)"/></svg>
        123-456-7890
      </li>
      <li>
        <svg viewBox="0 0 18 18" aria-hidden="true"><circle cx="9" cy="9" r="9" fill="var(--brand-blue)"/><rect x="6" y="3.5" width="6" height="11" rx="1" fill="var(--white)"/><rect x="7" y="5" width="4" height="6.5" fill="var(--brand-blue)"/></svg>
        123-546-7890
      </li>
    </ul>
    <ul class="contact-list contact-list--web">
      <li>
        <svg viewBox="0 0 18 18" aria-hidden="true"><circle cx="9" cy="9" r="9" fill="var(--brand-blue)"/><rect x="4" y="5.5" width="10" height="7" fill="var(--white)"/><path d="M4,5.5 L9,9.5 L14,5.5" fill="none" stroke="var(--brand-blue)" stroke-width="1"/></svg>
        name@yourdomain.com
      </li>
      <li>
        <svg viewBox="0 0 18 18" aria-hidden="true"><circle cx="9" cy="9" r="9" fill="var(--brand-blue)"/><circle cx="9" cy="9" r="5" fill="none" stroke="var(--white)" stroke-width="1.3"/><path d="M4,9 H14 M9,4 Q6,9 9,14 M9,4 Q12,9 9,14" fill="none" stroke="var(--white)" stroke-width="1"/></svg>
        www.yourdomain.com
      </li>
    </ul>
  </section>

  <section class="card card--back">
    <svg class="shapes" viewBox="0 0 556 325" aria-hidden="true">
      <path d="M0,0 L240,0 C130,20 60,60 0,128 Z" fill="var(--brand-blue)"/>
      <path d="M240,0 C130,20 60,60 0,128" fill="none" stroke="var(--white)" stroke-width="6"/>
      <path d="M292,0 C160,14 70,58 0,134" fill="none" stroke="var(--swoosh-grey)" stroke-width="5"/>
      <path d="M556,202 C500,262 420,308 318,325 L556,325 Z" fill="var(--brand-blue)"/>
      <path d="M556,202 C500,262 420,308 318,325" fill="none" stroke="var(--white)" stroke-width="6"/>
      <path d="M556,192 C495,255 400,305 262,325" fill="none" stroke="var(--swoosh-grey)" stroke-width="5"/>
    </svg>
    <p class="brand-name">Velnadex</p>
  </section>

</div>
</body>
</html>
```